Skiing Company Needs A5 28page Skiing Catalogue

ABOUT THE BUSINESS/COMPANY:
- We are a guided skiing company called "Silver Ridge Outings" and "Tamarack Powder Society".

ABOUT THE CATALOGUE:

- We need an A5 28 page catalogue. ALL THE FILES (like photos and logos) are in the zip folders.

- You can look at the 000 TPS Catalog Word Document. Instructions on what text and photos to use are labeled there per Page.

Target Market(s)

Advanced/ Expert Skiers and Snowboarders that are thinking of joining a tour

Industry/Entity Type

Travel Agent

Font styles to use
Serif

Colors
ffffff
ec1f27
0455a3

Requirements
Must have
• NEED a 3mm bleed
• This is included on the 000 TPS Catalog word document
Nice to have
• Our main color is dark blue (just like our logo). Some red is ok but the main focus should be the dark blue.
Should not have
• Words/ Letters in the color red

```html
<!DOCTYPE html>
<html lang="en">
<head>
<meta charset="utf-8">
<title>Partners and Contact Spread</title>
<link rel="stylesheet" href="https://fonts.googleapis.com/css2?family=Merriweather:wght@400;700&family=Montserrat:wght@700&display=swap">
<style>
  :root {
    --brand-blue: #0455a3;
    --white: #ffffff;
    --canvas-bg: #e9e7e3;
    --photo-sky: #8fa9c6;
    --photo-snow: #e8ecf1;
    --photo-forest: #4a4038;
    --photo-shadow: #6b6d72;
  }
  * { box-sizing: border-box; margin: 0; padding: 0; }
  html, body { width: 1200px; height: 1200px; overflow: hidden; }
  body { background: var(--canvas-bg); position: relative; }

  .spread {
    position: absolute;
    left: 40px; top: 204px;
    width: 1120px; height: 791px;
    display: flex;
    box-shadow: 0 6px 18px rgba(0,0,0,0.18);
  }

  .partners-page {
    position: relative;
    width: 560px; height: 100%;
    background: var(--brand-blue);
    color: var(--white);
    font-family: "Merriweather", Georgia, serif;
  }
  .section-title {
    position: absolute;
    left: 45px; top: 179px;
    font-family: "Montserrat", Arial, sans-serif;
    font-weight: 700;
    font-size: 25px;
    letter-spacing: 0.3px;
  }
  .partner {
    position: absolute;
    left: 45px; width: 490px;
    display: flex;
  }
  .partner-badge {
    flex: none;
    width: 100px;
    background: var(--white);
  }
  .partner-badge.dark { background: #111111; }
  .partner-body { position: absolute; left: 115px; top: 0; width: 375px; }
  .partner-name { font-weight: 700; font-size: 13.5px; line-height: 16px; }
  .partner-text { font-size: 13.5px; line-height: 16px; }

  .partner.lodge { top: 218px; }
  .partner.lodge .partner-badge { height: 80px; margin-top: 4px; clip-path: polygon(50% 0, 100% 100%, 0 100%); }
  .partner.auto { top: 352px; }
  .partner.auto .partner-badge { height: 41px; }
  .partner.boards { top: 485px; }
  .partner.boards .partner-badge { height: 100px; }
  .partner.foundry { top: 618px; }
  .partner.foundry .partner-badge { height: 100px; }

  .contact-page {
    position: relative;
    width: 560px; height: 100%;
    background:
      linear-gradient(180deg,
        var(--photo-sky) 0%,
        var(--photo-snow) 12%,
        #c9ccd1 26%,
        var(--photo-forest) 36%,
        #5b3c36 50%,
        #8a8c92 60%,
        var(--photo-snow) 72%,
        #dde1e7 100%);
    color: var(--white);
    font-family: "Merriweather", Georgia, serif;
  }
  .contact-page::after {
    content: "";
    position: absolute; inset: 0;
    background: linear-gradient(90deg, rgba(60,62,68,0.25), rgba(60,62,68,0) 70%);
  }
  .contact {
    position: absolute;
    left: 45px; top: 566px;
    z-index: 1;
    opacity: 0.85;
  }
  .contact-title {
    font-family: "Montserrat", Arial, sans-serif;
    font-weight: 700;
    font-size: 22px;
    margin-bottom: 14px;
  }
  .contact-line { font-size: 13px; line-height: 16px; }
  .contact-line b { font-weight: 700; }
  .contact-gap { height: 16px; }
</style>
</head>
<body>
  <main class="spread">
    <section class="partners-page">
      <h2 class="section-title">OUR PARTNERS</h2>

      <article class="partner lodge">
        <div class="partner-badge" aria-hidden="true"></div>
        <div class="partner-body">
          <h3 class="partner-name">Granite Hollow Lodge</h3>
          <p class="partner-text">Enjoy the down to earth atmosphere at<br>the Granite Hollow Lodge. Located a short walk<br>from the base of the Hollow Village chairlifts<br>this is the true powder hunters lodge.</p>
        </div>
      </article>

      <article class="partner auto">
        <div class="partner-badge" aria-hidden="true"></div>
        <div class="partner-body">
          <h3 class="partner-name">Northline Auto</h3>
          <p class="partner-text">Northline Auto is Hokkaido's original English speaking<br>rental agent. We offer everything from budget<br>to luxury rental vehicles. All rentals include 24hr<br>roadside assistance in English, English GPS,<br>liability insurance, and taxes.<br>Start Exploring Hokkaido today!</p>
        </div>
      </article>

      <article class="partner boards">
        <div class="partner-badge dark" aria-hidden="true"></div>
        <div class="partner-body">
          <h3 class="partner-name">Keller Snowboards</h3>
          <p class="partner-text">Based in Colorado, Keller Snowboards makes some<br>of the highest quality snowboards, splitboards, and<br>speciality boards in the industry.</p>
        </div>
      </article>

      <article class="partner foundry">
        <div class="partner-badge" aria-hidden="true"></div>
        <div class="partner-body">
          <h3 class="partner-name">Foundry of Gears</h3>
          <p class="partner-text">The Foundry of Gears vision was to create an<br>environment to honour both man and machine.<br>The foundation store is housed in a historic<br>workhouse in Cape Town, South Africa and is<br>the consummate fusion of coffee, café, craft beer,<br>cocktails, live music, menswear and custom bikes —<br>the quintessential fine purveyor for the modern man.</p>
        </div>
      </article>
    </section>

    <section class="contact-page" role="img" aria-label="Photo of a snowy mountain above a red lodge with parked vans, snowmobiles and a helicopter on the snow">
      <div class="contact">
        <h2 class="contact-title">CONTACT US</h2>
        <p class="contact-line"><b>Address:</b></p>
        <p class="contact-line">12-4 Kawamura, Yukino-cho,</p>
        <p class="contact-line">Hokkaido 000-0000</p>
        <div class="contact-gap"></div>
        <p class="contact-line"><b>Tel:</b> +81-(0)100-22-3344</p>
        <div class="contact-gap"></div>
        <p class="contact-line"><b>Email:</b> info@tamarackpowdersociety.com</p>
        <p class="contact-line"><b>Website:</b> www.tamarackpowdersociety.com</p>
        <p class="contact-line"><b>Website:</b> www.silverridgeoutings.com</p>
      </div>
    </section>
  </main>
</body>
</html>
```